I am looking for a flyer design for my upcoming symposium. Here are the details for the flyer and pictures of speakers are attached.

Name of Symposium: Lattice and Pathway Biosciences Symposium, Sponsored by the Corvale Chromatin Institute and the Department of Bioengineering
Date: January 8, 2018
Location: Havergill Auditorium, Tarnby Center for Applied Discovery, 2175 Orchard Terrace Ave, Philadelphia, PA 19127

Reception to follow after the symposium.

Also, please add - Register and upload abstracts for the symposium at www.qzvmrk.com. Registration and abstract submission closes on January 4, 2018.

Keynote Speaker:
Marthe Quillon, Ph.D.
NTVO Director General; Professor, Lyceum of Norvane; Director, Genetics and Developmental Biology at Institut Bramoux
Lyceum of Norvane, NTVO, Institut Bramoux
"Title of talk TBA."

Speakers:
Lena Drewcott, Ph.D.
Assistant Professor of Cell and Developmental Biology
Halvering State University, HMCS
"Title of talk TBA."

Paul Marden, Ph.D.
Assistant Professor of Genetics
"Title of talk TBA."

Ilse Varga, Ph.D.
Professor, Ostrander University
Otto Wenzlau Center for Molecular Medicine
"Title of talk TBA."

Jun Hao, Ph.D.
Professor of Cellular and Molecular Medicine
Coastal Meridian University
"Title of talk TBA."

Wei Lun, Ph.D.
Associate Professor of Pediatrics
The Youth Medical Pavilion of Philadelphia
"Spatial genome re-organization between fetal and adult hematopoietic stem cells."

Mei Zhou, Ph.D.
Professor, Department of Genetics
Ellsworth Medical School
"Title of talk TBA."

```html
<!DOCTYPE html>
<html lang="en">
<head>
<meta charset="utf-8">
<title>Lattice and Pathway Biosciences Symposium</title>
<link href="https://fonts.googleapis.com/css2?family=Montserrat:wght@300;400;500;600;700;800&display=swap" rel="stylesheet">
<style>
:root{
  --paper:#ffffff;
  --maroon:#5a0810;
  --maroon-deep:#2a0609;
  --panel-dark:#2b0a10;
  --red-line:#d3262f;
  --yellow:#f6d635;
  --sky:#8fd3f2;
  --ink-light:#f1e6e2;
  --navy:#1d3a57;
  --slate:#4f5f70;
}
*{box-sizing:border-box;margin:0;padding:0}
html,body{width:927px;height:1200px;overflow:hidden;background:var(--paper)}
body{font-family:'Montserrat',sans-serif;position:relative}
.poster{position:absolute;left:12px;top:12px;width:903px;height:945px;overflow:hidden;background:var(--panel-dark)}
.poster-left{position:absolute;left:0;top:0;width:438px;height:940px;
  background:linear-gradient(180deg,#6a0a12 0%,#5a0810 40%,#4a060c 100%)}
.dna-art{position:absolute;left:0;top:360px;width:438px;height:580px;
  background:radial-gradient(ellipse 60% 70% at 48% 55%,#b3202a 0%,#7d0f17 45%,rgba(74,6,12,0) 80%)}
.divider{position:absolute;left:438px;top:0;width:3px;height:940px;background:var(--red-line)}
.poster-right{position:absolute;left:441px;top:0;width:462px;height:940px;
  background:linear-gradient(180deg,#30080e 0%,#3a0a12 55%,#4a0c14 100%)}
.base-band{position:absolute;left:0;top:940px;width:903px;height:5px;background:var(--red-line)}

.title{position:absolute;left:0;top:38px;width:438px;text-align:center}
.title-main{color:var(--yellow);font-weight:800;font-size:49px;line-height:62px;letter-spacing:1px}
.title-sub{color:#fff;font-weight:400;font-size:49px;line-height:62px;letter-spacing:2px;margin-top:10px}
.sponsor{position:absolute;left:0;top:292px;width:438px;text-align:center;color:#fff;font-size:16.5px;line-height:22px}

.section-head{position:absolute;left:600px;font-weight:700;font-size:16px;display:flex;align-items:center;width:303px}
.section-head::after{content:"";flex:1;height:2px;margin-left:10px}
.head-keynote{top:40px;color:var(--yellow)}
.head-keynote::after{background:var(--yellow)}
.head-speakers{top:240px;color:var(--sky)}
.head-speakers::after{background:var(--sky)}

.portrait{position:absolute;border-radius:50%;border:3px solid #fff;
  background:radial-gradient(circle at 50% 40%,#c9a58f 0%,#7a5a4a 60%,#4a3a36 100%)}
.portrait-keynote{left:477px;top:83px;width:116px;height:116px}
.portrait-speaker{left:494px;width:90px;height:90px}

.bio{position:absolute;left:596px;font-size:12.6px;line-height:16.3px;color:var(--ink-light)}
.bio .name{font-weight:700;font-size:13.5px;color:var(--sky)}
.bio-keynote{top:96px;color:#f3e8c8}
.bio-keynote .name{color:var(--yellow)}

.brand{position:absolute;left:45px;display:flex;align-items:center;gap:10px;color:var(--navy);font-weight:600;font-size:17px;line-height:20px}
.brand-mark{width:26px;height:26px;background:var(--navy);flex:none}
.brand-circle{border-radius:50%}
.brand-eng{top:1020px}
.brand-inst{top:1100px}

.event-date{position:absolute;right:43px;top:990px;font-weight:700;font-size:33px;color:var(--navy)}
.venue{position:absolute;right:43px;top:1040px;text-align:right;font-size:14px;line-height:18.5px;color:var(--slate)}
.register{position:absolute;right:35px;top:1098px;text-align:right;font-size:16px;line-height:21px;color:var(--navy)}
.register strong{font-weight:700}
.reception{position:absolute;right:35px;top:1155px;font-size:16px;color:var(--navy)}
</style>
</head>
<body>
<main class="poster">
  <section class="poster-left">
    <div class="dna-art" role="img" aria-label="Red microscope render of a DNA double helix"></div>
    <h1 class="title">
      <div class="title-main">LATTICE AND<br>PATHWAY<br>BIOSCIENCES</div>
      <div class="title-sub">SYMPOSIUM</div>
    </h1>
    <p class="sponsor">Sponsored by the Corvale Chromatin Institute<br>and the Department of Bioengineering</p>
  </section>
  <div class="divider"></div>
  <section class="poster-right"></section>
  <div class="base-band"></div>

  <h2 class="section-head head-keynote">Keynote Speaker</h2>
  <div class="portrait portrait-keynote" role="img" aria-label="Portrait photo of Marthe Quillon"></div>
  <div class="bio bio-keynote">
    <div class="name">Marthe Quillon, Ph.D.</div>
    NTVO Director General; Professor,<br>Lyceum of Norvane; Director, Genetics and<br>Developmental Biology at Institut Bramoux<br>Lyceum of Norvane, NTVO, Institut Bramoux<br>"Title of talk TBA."
  </div>

  <h2 class="section-head head-speakers">Speakers</h2>

  <div class="portrait portrait-speaker" style="top:284px" role="img" aria-label="Portrait photo of Lena Drewcott"></div>
  <div class="bio" style="top:292px"><div class="name">Lena Drewcott, Ph.D.</div>Assistant Professor of Cell and<br>Developmental Biology<br>Halvering State University, HMCS<br>"Title of talk TBA."</div>

  <div class="portrait portrait-speaker" style="top:388px" role="img" aria-label="Portrait photo of Paul Marden"></div>
  <div class="bio" style="top:406px"><div class="name">Paul Marden, Ph.D.</div>Assistant Professor of Genetics<br>Halvering State University, HMCS<br>"Title of talk TBA."</div>

  <div class="portrait portrait-speaker" style="top:495px" role="img" aria-label="Portrait photo of Ilse Varga"></div>
  <div class="bio" style="top:505px"><div class="name">Ilse Varga, Ph.D.</div>Professor, Ostrander University<br>Otto Wenzlau Center for<br>Molecular Medicine | "Title of talk TBA."</div>

  <div class="portrait portrait-speaker" style="top:601px" role="img" aria-label="Portrait photo of Jun Hao"></div>
  <div class="bio" style="top:610px"><div class="name">Jun Hao, Ph.D.</div>Professor of Cellular and<br>Molecular Medicine<br>Coastal Meridian University<br>"Title of talk TBA."</div>

  <div class="portrait portrait-speaker" style="top:708px" role="img" aria-label="Portrait photo of Wei Lun"></div>
  <div class="bio" style="top:715px"><div class="name">Wei Lun, Ph.D.</div>Associate Professor of Pediatrics<br>The Youth Medical Pavilion of Philadelphia<br>"Spatial genome re-organization<br>between fetal and adult<br>hematopoietic stem cells."</div>

  <div class="portrait portrait-speaker" style="top:815px" role="img" aria-label="Portrait photo of Mei Zhou"></div>
  <div class="bio" style="top:857px"><div class="name">Mei Zhou, Ph.D.</div>Professor, Department of Genetics<br>Ellsworth Medical School | "Title of talk TBA."</div>
</main>

<footer>
  <div class="brand brand-eng"><span class="brand-mark"></span>Halvering Engineering</div>
  <div class="brand brand-inst"><span class="brand-mark brand-circle"></span>Corvale Chromatin<br>Institute</div>

  <div class="event-date">January 8, 2018</div>
  <p class="venue">Havergill Auditorium, Tarnby Center for Applied Discovery<br>Research, 2175 Orchard Terrace Ave, Philadelphia, PA 19127</p>
  <p class="register">Register and upload abstracts for the symposium at www.qzvmrk.com.<br>Registration and abstract submission closes on <strong>January 4, 2018.</strong></p>
  <p class="reception">Reception to follow after the symposium.</p>
</footer>
</body>
</html>
```